High End Notary Service Business Card Design

Want a professional and elegant/luxurious business card that is clean and simple in the design. A notary is a trusted professional that helps people sign very important documents. The card should be in alignment with this service provided.

Most of the time, service will be for the purchase of a home or refinance of a mortgage

There is NO LOGO. This is aesthetic. A look and feel. Conveying professionalism and concierge level of service.

Target Market(s)

Other business professionals, Lawyers, Escrow Officers, Loan Officers

Industry/Entity Type

Legal

Contact Information for Business Card

This will be a one-sided business card

Colors
35a7d7
3176b5
85cae6
d3a5cc
b868aa
ffffff
0356a4

Requirements
Must have
• Lorena T. Mirabel-Hodgkins
Notary Public

642-871-3094
MirabelSigningDesk@Wexmail.com
Nice to have
• Headshot photo below. Convey the aspect of signing documents. No black cards. Preference is shades of blue: light blue, navy, aqua, gold, white, or lavendar, etc.
Should not have
• No scales or legal scales.

```html
<!DOCTYPE html>
<html lang="en">
<head>
<meta charset="utf-8">
<title>Lorena T. Mirabel-Hodgkins — Notary Public</title>
<link href="https://fonts.googleapis.com/css2?family=Montserrat:wght@400;700&display=swap" rel="stylesheet">
<style>
  :root {
    --backdrop: #e4e7eb;
    --card-blue-deep: #1f5fae;
    --card-blue-light: #4f8fcb;
    --band-lavender: #d3a5cc;
    --icon-plum: #b868aa;
    --text-white: #ffffff;
    --photo-hair: #8a5a3c;
    --photo-skin: #e9b9a2;
  }
  html, body {
    margin: 0;
    padding: 0;
    width: 1200px;
    height: 900px;
    overflow: hidden;
    background: var(--backdrop);
    font-family: "Montserrat", sans-serif;
  }
  .canvas {
    position: relative;
    width: 1200px;
    height: 900px;
    display: flex;
    align-items: center;
    justify-content: center;
  }
  .business-card {
    position: relative;
    width: 840px;
    height: 480px;
    background: linear-gradient(150deg, var(--card-blue-light) 0%, var(--card-blue-deep) 70%);
    overflow: hidden;
    box-shadow: 0 18px 40px rgba(40, 50, 70, 0.25);
  }
  .headshot {
    position: absolute;
    right: 0;
    top: 40px;
    width: 360px;
    height: 440px;
    background: radial-gradient(ellipse at 50% 35%, var(--photo-skin) 0%, var(--photo-skin) 30%, var(--photo-hair) 55%, rgba(138, 90, 60, 0) 75%);
  }
  .name-band {
    position: absolute;
    left: 0;
    top: 218px;
    width: 555px;
    height: 100px;
    background: var(--band-lavender);
  }
  .identity {
    position: absolute;
    left: 70px;
    top: 240px;
    color: var(--text-white);
  }
  .identity .person-name {
    margin: 0;
    font-weight: 700;
    font-size: 24px;
    letter-spacing: 0.5px;
  }
  .identity .person-title {
    margin: 4px 0 0;
    font-weight: 400;
    font-size: 20px;
  }
  .contact-list {
    position: absolute;
    left: 108px;
    top: 370px;
    margin: 0;
    padding: 0;
    list-style: none;
    color: var(--text-white);
    font-size: 19px;
  }
  .contact-list li {
    display: flex;
    align-items: center;
    gap: 10px;
    margin-bottom: 6px;
  }
  .contact-icon {
    width: 16px;
    height: 16px;
    flex: none;
  }
</style>
</head>
<body>
  <main class="canvas">
    <section class="business-card">
      <div class="headshot" role="img" aria-label="Headshot photo of the notary, smiling, with shoulder-length brown hair"></div>
      <div class="name-band"></div>
      <div class="identity">
        <h1 class="person-name">Lorena T. Mirabel-Hodgkins</h1>
        <p class="person-title">Notary Public</p>
      </div>
      <ul class="contact-list">
        <li>
          <svg class="contact-icon" viewBox="0 0 16 16" aria-hidden="true">
            <path d="M3 1.5 L6 4.5 L4.5 6.5 C5.5 8.5 7.5 10.5 9.5 11.5 L11.5 10 L14.5 13 L12.5 15 C7 14 2 9 1 3.5 Z" fill="var(--icon-plum)"/>
          </svg>
          <span>642-871-3094</span>
        </li>
        <li>
          <svg class="contact-icon" viewBox="0 0 16 16" aria-hidden="true">
            <rect x="1" y="3" width="14" height="10" fill="var(--icon-plum)"/>
            <path d="M1 3 L8 9 L15 3" fill="none" stroke="var(--text-white)" stroke-width="1.2"/>
          </svg>
          <span>MirabelSigningDesk@Wexmail.com</span>
        </li>
      </ul>
    </section>
  </main>
</body>
</html>
```